Holiday PROMO Flyer for Healthy Restaurant

Hi ! We need a holiday style promo flyer for Verandel . Please have a holiday vibe type of design in the background. Include at least 1 of the photos that I provide, and our logo of course. This promo is for a new package that we will be offering until December 31st 2022.

It will have a promo of some type of design that says the following in a creative way:
" HOLIDAY PACKAGE PROMO!"
Buy our holiday package of $500 and receive a $100 gift card!" (THIS SHOULD BE VERY NOTICEABLE AS THIS IS THE ACTUAL PROMO)
Our biggest promo to date.
Offer ends December 31st, 2022.

Take a look at our website to stay consistant with the brand as well.

Industry/Entity Type

Restaurant

Requirements
Must have
• Logo, food photo and gift card photo

```html
<!DOCTYPE html>
<html lang="en">
<head>
<meta charset="UTF-8">
<title>Verandel Holiday Package Promo</title>
<link rel="stylesheet" href="https://fonts.googleapis.com/css2?family=Bebas+Neue&family=Montserrat:wght@700&family=Open+Sans:wght@400&display=swap">
<style>
  :root {
    --page-bg: #e2e2e2;
    --paper: #ffffff;
    --navy: #14365f;
    --navy-soft: #1d4470;
    --lime: #93c023;
    --grey: #8f8f8f;
    --photo-a: #e9ecef;
    --photo-b: #c9a27a;
  }
  * { margin: 0; padding: 0; box-sizing: border-box; }
  html, body { width: 1200px; height: 1200px; overflow: hidden; background: var(--page-bg); }
  .flyer {
    position: absolute; left: 285px; top: 154px; width: 630px; height: 891px;
    background: var(--navy); overflow: hidden;
  }
  .brand-header {
    position: absolute; left: 0; top: 0; width: 100%; height: 137px;
    background: var(--paper); text-align: center;
  }
  .brand-name {
    position: absolute; left: 0; right: 0; top: 38px;
    font-family: "Montserrat", sans-serif; font-weight: 700;
    font-size: 52px; line-height: 1; letter-spacing: 2px; color: var(--grey);
  }
  .brand-tagline {
    position: absolute; left: 0; right: 0; top: 96px;
    font-family: "Montserrat", sans-serif; font-weight: 700;
    font-size: 17px; line-height: 1; color: var(--lime);
  }
  .promo-band {
    position: absolute; left: 0; top: 137px; width: 100%; height: 73px;
    background: var(--lime); color: var(--navy);
    font-family: "Bebas Neue", sans-serif; font-size: 66px; line-height: 78px;
    text-align: center;
  }
  .holiday-decor {
    position: absolute; left: 30px; top: 300px; width: 570px; height: 260px;
    background: radial-gradient(ellipse at 50% 50%, var(--navy-soft) 0%, var(--navy) 70%);
  }
  .offer-headline {
    position: absolute; left: 0; right: 0; top: 240px;
    font-family: "Bebas Neue", sans-serif; font-weight: 400; font-size: 86px; line-height: 77px;
    text-align: center; color: var(--paper);
  }
  .offer-headline .accent { color: var(--lime); }
  .divider { position: absolute; left: 226px; top: 634px; width: 179px; height: 1px; background: var(--lime); }
  .menu-photo {
    position: absolute; top: 659px; width: 110px; height: 110px; border-radius: 50%;
    background: radial-gradient(circle at 50% 50%, var(--photo-b) 0%, #b88a5c 35%, var(--photo-a) 62%, #dfe3e8 100%);
  }
  .offer-deadline {
    position: absolute; left: 147px; top: 791px; width: 342px; height: 42px;
    border-radius: 10px; background: var(--lime); color: var(--paper);
    font-family: "Bebas Neue", sans-serif; font-size: 30px; line-height: 44px; text-align: center;
  }
  .site-url {
    position: absolute; left: 0; right: 0; top: 840px;
    font-family: "Open Sans", sans-serif; font-size: 19px; color: var(--paper); text-align: center;
  }
</style>
</head>
<body>
<main class="flyer">
  <header class="brand-header">
    <div class="brand-name">VERANDEL</div>
    <div class="brand-tagline">HEALTHY KITCHEN &nbsp;|&nbsp; MEAL PREP</div>
  </header>

  <div class="promo-band">HOLIDAY PACKAGE PROMO!</div>

  <div class="holiday-decor" role="img" aria-label="Scattered lime outline holiday travel icons around the offer"></div>

  <h1 class="offer-headline">
    BUY OUR HOLIDAY<br>
    <span class="accent">PACKAGE OF</span><br>
    $500<br>
    <span class="accent">AND RECEIVE A</span><br>
    $100 GIFT CARD!
  </h1>

  <div class="divider"></div>

  <div class="menu-photo" style="left:43px" role="img" aria-label="Photo of a loaded rice and chicken bowl"></div>
  <div class="menu-photo" style="left:183px" role="img" aria-label="Photo of a grilled chicken sandwich"></div>
  <div class="menu-photo" style="left:330px" role="img" aria-label="Photo of a fish plate with greens and sweet potato"></div>
  <div class="menu-photo" style="left:477px" role="img" aria-label="Photo of a slice of carrot cake"></div>

  <div class="offer-deadline">OFFER ENDS DECEMBER 31ST, 2022</div>
  <div class="site-url">www.verandelkitchen.com</div>
</main>
</body>
</html>
```